Web Design Project for an operational risk management consulting company

Website is for a consulting company specialising in operational risk management. Our specialist areas include crisis and emergency management, community engagement, safety and security. We work internationally, generally in high hazard environments. We are a highly ethical and professional company which prides itself on delivering a strong level of customer service.

As a company we recognise that the key to keeping people safe is ensuring that they work in an ethical and sustainable manner. Therefore we are as much about soft skills as we are about hard skills. We would like our website and supporting images to reflect this.
We have worked throughout Africa and the Middle east, as well as Asia pacific. An international flavour to the website would also be great.
Background images on www.corvellpartnersglobal.example are a good example of what we are thinking of, though very open to fresh ideas.

Target Market(s)

Our customers are generally medium to large organisations who work internationally. We would like to also support more not for profits and non government organisations who work in hazardous environments

Industry/Entity Type

It Company

Number of Pages Required

5+ page

Font styles to use
Sans Serif

Requirements
Must have
• Easy to edit by non IT people
• Section for blogs/news updates
• Pages should include:
• (A) home page
• (B) about us
• (C) services
• (D) contact
• (E) insights
Nice to have
• An international and professional theme. Some gritty images that symbolise the risks associated with working in unstable environments, as well as some human ones and that of the environment
Should not have
• Cartoonish or generic images
• Not focus on traditional physical security aspects

```html
<!DOCTYPE html>
<html lang="en">
<head>
<meta charset="utf-8">
<title>Corvell Partners – Operational Risk Management</title>
<link rel="stylesheet" href="https://fonts.googleapis.com/css2?family=Open+Sans:wght@400;600;700&display=swap">
<style>
:root{
  --blue:#2a6db3;
  --ink:#444;
  --muted:#777;
  --light:#f0f0f0;
  --white:#fff;
  --footer:#4b4b4b;
  --button:#5e5e5e;
}
*{box-sizing:border-box;margin:0;padding:0}
html,body{width:896px;height:1200px;overflow:hidden}
body{font-family:'Open Sans',Arial,sans-serif;color:var(--ink);background:var(--white);position:relative}
.hero{position:absolute;left:0;top:0;width:896px;height:405px;overflow:hidden}
.hero-photo{position:absolute;inset:0;background:linear-gradient(200deg,#f0a44a 0%,#b9784a 18%,#5b5a62 42%,#33363f 70%,#24262c 100%)}
.hero-shade{position:absolute;inset:0;background:rgba(0,0,0,.25)}
.brand{position:absolute;left:14px;top:12px;display:flex;align-items:center;gap:8px;color:var(--white);font-weight:700;font-size:20px}
.brand-dot{width:26px;height:26px;border-radius:50%;background:var(--white)}
.main-nav{position:absolute;right:22px;top:28px;display:flex;gap:30px}
.main-nav a{color:var(--white);text-decoration:none;font-size:12px}
.social{display:flex;gap:12px}
.social span{width:12px;height:12px;border-radius:50%;background:var(--white);opacity:.85}
.hero .social{position:absolute;right:26px;top:66px}
.hero-title{position:absolute;left:0;right:0;top:196px;text-align:center;color:var(--white);font-size:27px;font-weight:600;line-height:1.25;text-shadow:0 1px 3px rgba(0,0,0,.5)}
.dots{position:absolute;left:0;right:0;top:286px;display:flex;justify-content:center;gap:6px}
.dots span{width:9px;height:9px;border-radius:50%;background:rgba(255,255,255,.5)}
.dots span.on{background:var(--white)}
.welcome{position:absolute;left:0;top:405px;width:896px;height:210px}
.welcome h1{position:absolute;left:24px;top:24px;font-size:24px;font-weight:600;color:var(--blue)}
.welcome p{position:absolute;left:24px;top:62px;width:540px;font-size:10px;line-height:1.6;color:var(--muted)}
.btn{position:absolute;left:24px;top:158px;background:var(--button);color:var(--white);font-size:10px;letter-spacing:.5px;padding:9px 22px;text-decoration:none}
.welcome-art{position:absolute;left:592px;top:30px;width:290px;height:164px;background:linear-gradient(135deg,#2c2c2c,#555 60%,#1e1e1e)}
.services{position:absolute;left:0;top:615px;width:896px;height:300px;background:var(--light)}
.services h2{position:absolute;left:0;right:0;top:12px;text-align:center;font-size:22px;font-weight:600;color:var(--blue)}
.cards{position:absolute;left:70px;top:55px;display:flex;gap:30px}
.card{width:232px}
.card .photo{height:122px}
.card h3{font-size:12px;font-weight:600;color:var(--blue);margin-top:12px}
.card p{font-size:9.5px;line-height:1.55;color:var(--muted);margin-top:4px}
.learn{display:block;font-size:9.5px;font-weight:700;color:var(--ink);text-decoration:none;margin-top:6px}
.insight{position:absolute;left:54px;top:925px;width:500px}
.blog{position:absolute;left:592px;top:925px;width:280px}
.insight h2,.blog h2{font-size:20px;font-weight:600;color:var(--blue)}
.arrows{position:absolute;right:0;top:8px;display:flex;gap:10px}
.post{display:flex;gap:14px;margin-top:12px}
.post .thumb{width:124px;height:98px;flex:none;background:linear-gradient(135deg,#222,#4d4d4d)}
.post h4,.blog h4{font-size:12px;font-weight:600;color:var(--blue)}
.post p,.blog p{font-size:9.5px;line-height:1.55;color:var(--muted);margin-top:4px}
.blog h4{margin-top:10px}
.footer{position:absolute;left:0;top:1100px;width:896px;height:100px;background:var(--footer);color:#ddd;text-align:center}
.footer-nav{display:flex;justify-content:center;gap:34px;padding-top:20px}
.footer-nav a{color:var(--white);font-size:10px;text-decoration:none}
.copyright{font-size:9px;color:#bbb;margin-top:8px}
.footer .social{justify-content:center;margin-top:12px}
</style>
</head>
<body>
<header class="hero">
  <div class="hero-photo" role="img" aria-label="City skyline at sunset seen from above"></div>
  <div class="hero-shade"></div>
  <div class="brand"><span class="brand-dot"></span>Corvell</div>
  <nav class="main-nav"><a href="#">Home</a><a href="#">About Us</a><a href="#">Services</a><a href="#">Insights</a><a href="#">Contact</a></nav>
  <div class="social"><span></span><span></span><span></span><span></span><span></span></div>
  <h1 class="hero-title">We are a Consulting Company Specialising<br>in Operational Risk Management.</h1>
  <div class="dots"><span class="on"></span><span class="on"></span><span></span></div>
</header>

<section class="welcome">
  <h1>Welcome to Our Website</h1>
  <p>We help organisations working in high hazard environments plan for crises, engage communities and keep their people safe. Our team has delivered programmes across Africa, the Middle East and Asia Pacific, combining practical field experience with careful, ethical advice. We believe safe operations depend as much on trust, listening and culture as on systems, procedures and equipment.</p>
  <a class="btn" href="#">READ MORE</a>
  <div class="welcome-art" role="img" aria-label="Hand writing Manage Your Risk on a chalkboard"></div>
</section>

<section class="services">
  <h2>We Specialised In</h2>
  <div class="cards">
    <article class="card">
      <div class="photo" role="img" aria-label="Emergency responders at an incident scene" style="background:linear-gradient(135deg,#3a4048,#6d7480)"></div>
      <h3>Crisis &amp; Emergency Management</h3>
      <p>Planning, training and exercises that prepare your teams to respond calmly and effectively when an incident occurs.</p>
      <a class="learn" href="#">Learn More (+)</a>
    </article>
    <article class="card">
      <div class="photo" role="img" aria-label="Community members raising hands together" style="background:linear-gradient(135deg,#2f5878,#8aa7bd)"></div>
      <h3>Community Engagement</h3>
      <p>Building lasting relationships with the communities around your sites through open dialogue and shared local benefit.</p>
      <a class="learn" href="#">Learn More (+)</a>
    </article>
    <article class="card">
      <div class="photo" role="img" aria-label="Safety and security notes on paper" style="background:linear-gradient(135deg,#e9e9e9,#b9b9b9)"></div>
      <h3>Safety and Security</h3>
      <p>Practical assessments and advice that protect your people, assets and reputation in complex operating settings.</p>
      <a class="learn" href="#">Learn More (+)</a>
    </article>
  </div>
</section>

<section class="insight">
  <h2>Insight</h2>
  <div class="arrows">
    <svg width="10" height="14" viewBox="0 0 10 14"><path d="M8 1 2 7l6 6" fill="none" stroke="#444" stroke-width="2"/></svg>
    <svg width="10" height="14" viewBox="0 0 10 14"><path d="M2 1l6 6-6 6" fill="none" stroke="#444" stroke-width="2"/></svg>
  </div>
  <div class="post">
    <div class="thumb" role="img" aria-label="Risk management notes on a dark board"></div>
    <div>
      <h4>Building a Safer Site Culture...</h4>
      <p>Lessons from recent field work on how small changes in site culture can sharply reduce operational risk for teams abroad.</p>
      <a class="learn" href="#">Learn More (+)</a>
    </div>
  </div>
</section>

<section class="blog">
  <h2>Blog</h2>
  <h4>Preparing Remote Teams for Crisis...</h4>
  <p>Notes from our advisers on preparing remote teams, managing evacuations and supporting staff wellbeing in difficult regions.</p>
  <a class="learn" href="#">Continue Reading</a>
</section>

<footer class="footer">
  <nav class="footer-nav"><a href="#">Home</a><a href="#">About Us</a><a href="#">Services</a><a href="#">Insights</a><a href="#">Contact</a></nav>
  <p class="copyright">© 2024 Corvell Partners. All rights reserved.</p>
  <div class="social"><span></span><span></span><span></span><span></span><span></span></div>
</footer>
</body>
</html>
```